Operator Qualification Testing Flyer

I have a 8x10 basic flyer that I created usin InDesign for one of our services our company provides. I would like to see more options for the layout and general design of the flyer. This flyer will be used as a template for the other services we provide. I will include the InDesign Folder with all the logos and images. Please feel free to use any logo design within the folder and you can change the font and/or colors as needed. I would like the final output in a Indesign package folder to be used in InDesign 2021

Target Market(s)

Business to Business marketing in the Oil and Gas industry

Font styles to use
Sans Serif

Colors
85cae6
85acd3
3377b5
0355a3
0792cd
ffffff
cedeed

Requirements
Must have
• I included/attached a couple of brochures styles that I do like.

```html
<!DOCTYPE html>
<html lang="en">
<head>
<meta charset="utf-8">
<title>Pipeline OQ Testing Flyer</title>
<link href="https://fonts.googleapis.com/css2?family=Montserrat:wght@300;800&family=Open+Sans:wght@400;600;700&display=swap" rel="stylesheet">
<style>
  :root{
    --sky:#85cae6;
    --steel:#85acd3;
    --mid-blue:#3377b5;
    --deep-blue:#0355a3;
    --bright-blue:#0792cd;
    --white:#ffffff;
    --mist:#cedeed;
    --teal-dark:#1d5d6c;
    --text:#4a4a4a;
    --backdrop:#e6e7e9;
  }
  *{box-sizing:border-box;margin:0;padding:0}
  html,body{width:1200px;height:960px;overflow:hidden;background:var(--backdrop)}
  .canvas{position:relative;width:1200px;height:960px}
  .flyer{position:absolute;left:250px;top:30px;width:700px;height:900px;background:linear-gradient(180deg,var(--white) 60%,#f1f2f3);overflow:hidden;box-shadow:0 10px 30px rgba(0,0,0,.18);font-family:"Open Sans",Arial,sans-serif;color:var(--text)}
  .hero-photo{position:absolute;left:0;top:0;width:700px;height:340px;background:linear-gradient(160deg,#9c9372 0%,#7d7658 40%,#a59c7c 70%,#6d6a55 100%)}
  .hero-bands{position:absolute;left:0;top:0;width:700px;height:440px}
  .title{position:absolute;left:70px;font-family:"Montserrat",Arial,sans-serif;color:var(--white);line-height:1}
  .title-main{top:308px;font-weight:800;font-size:46px;letter-spacing:12px}
  .title-sub{top:362px;font-weight:300;font-size:44px;letter-spacing:4px}
  .brand{position:absolute;left:520px;top:392px;display:flex;align-items:center;gap:8px}
  .brand-dot{width:26px;height:26px;border-radius:50%;background:var(--deep-blue)}
  .brand-name{font-weight:700;font-size:14px;color:var(--deep-blue);line-height:1.15;width:130px}

  .content{position:absolute;left:40px;top:448px;width:610px}
  .section{position:relative;min-height:52px}
  .section + .section{margin-top:16px}
  .section-icon{position:absolute;left:0;top:0;width:48px;height:48px;border:2px solid var(--mid-blue);display:flex;align-items:center;justify-content:center}
  .section-title{margin-left:68px;font-weight:700;font-size:18px;color:var(--bright-blue);line-height:1.25}
  .section-body{margin-top:6px;font-size:11px;line-height:1.5}
  .section-body p{margin-left:68px}
  .section-body p+p{margin-top:6px}
  .sec-oq{width:610px}
  .sec-tasks{width:440px}
  .sec-provide{width:430px}
  .sec-provide .section-body p+p{margin-left:0}

  .sign-photo{position:absolute;left:530px;top:585px;width:120px;height:120px;border-radius:50%;background:radial-gradient(circle,#e8b32a 0%,#d79a1a 70%,#2a2a2a 72%)}
  .contact{position:absolute;left:490px;width:210px;height:32px;display:flex;background:var(--sky)}
  .contact-text{flex:1;display:flex;align-items:center;padding-left:14px;font-size:11px;color:var(--white)}
  .contact-icon{width:38px;background:var(--bright-blue);display:flex;align-items:center;justify-content:center}
  .contact-phone{top:772px}
  .contact-mail{top:818px}
</style>
</head>
<body>
<div class="canvas">
  <article class="flyer">
    <div class="hero-photo" role="img" aria-label="Aerial view of a pipeline excavation site with a yellow sideboom tractor, safety cones and an open trench"></div>
    <svg class="hero-bands" viewBox="0 0 700 440" aria-hidden="true">
      <defs>
        <linearGradient id="banner-fill" x1="0" y1="0" x2="1" y2="1">
          <stop offset="0" stop-color="#0792cd"/>
          <stop offset="1" stop-color="#85cae6"/>
        </linearGradient>
      </defs>
      <polygon points="0,300 700,262 700,340 0,360" fill="#1d5d6c" opacity=".9"/>
      <polygon points="0,298 610,298 520,425 0,425" fill="url(#banner-fill)"/>
    </svg>
    <div class="title title-main">PIPELINE</div>
    <div class="title title-sub">OQ TESTING</div>

    <div class="brand">
      <span class="brand-dot"></span>
      <span class="brand-name">Meridian Field Services</span>
    </div>

    <div class="content">
      <section class="section sec-oq">
        <div class="section-icon">
          <svg width="26" height="26" viewBox="0 0 28 28" fill="none" stroke="#3377b5" stroke-width="2"><path d="M8 11a6 6 0 0 1 12 0z"/><path d="M6 11h16"/><path d="M5 26c0-5 4-8 9-8s9 3 9 8"/></svg>
        </div>
        <h2 class="section-title">What Is Operator Qualification?</h2>
        <div class="section-body">
          <p>Operator Qualifications (OQ) for DOT Oil/Gas Pipelines are requirements set by Department of Transportation (DOT) and Pipeline and Hazardous Materials Safety Administration (PHMSA). To assure safety in the transport of hazardous gases and liquids in the nation's pipelines, pipeline operators who perform covered tasks must be qualified. Qualified means that an individual has been evaluated and can perform assigned covered tasks and recognize and react to abnormal operating conditions.</p>
        </div>
      </section>

      <section class="section sec-tasks">
        <div class="section-icon">
          <svg width="24" height="24" viewBox="0 0 26 26" fill="none" stroke="#3377b5" stroke-width="2"><rect x="4" y="3" width="13" height="17"/><rect x="9" y="7" width="13" height="17" fill="#fff"/><path d="M12 13h7M12 17h7"/></svg>
        </div>
        <h2 class="section-title">What Are Covered Tasks?</h2>
        <div class="section-body">
          <p>Covered tasks are defined in an operator's written plan which defines specific job functions or activities personnel are qualified to perform on a pipeline facility.</p>
        </div>
      </section>

      <section class="section sec-provide">
        <div class="section-icon">
          <svg width="26" height="26" viewBox="0 0 28 28" fill="none" stroke="#3377b5" stroke-width="2"><circle cx="14" cy="14" r="4"/><path d="M14 3v4M14 21v4M3 14h4M21 14h4M6 6l3 3M19 19l3 3M22 6l-3 3M9 19l-3 3"/></svg>
        </div>
        <h2 class="section-title">What We Provide</h2>
        <div class="section-body">
          <p>Meridian Field Services utilizes Craftline pipeline program to administer OQ assessment testing on 127 covered tasks.</p>
          <p>Upon completion of OQ testing the information is first transferred to Craftline's Registry System and automatically uploaded to SafeVendor.</p>
          <p>In addition to the benefits provided by SafeVendor's database, the Craftline Registry System houses all the completion information allowing candidates to share their training information and employers to verify successful covered task and level completions.</p>
        </div>
      </section>
    </div>

    <div class="sign-photo" role="img" aria-label="Round warning sign for a petroleum pipeline marker"></div>

    <div class="contact contact-phone">
      <span class="contact-text">555-014-2290</span>
      <span class="contact-icon">
        <svg width="15" height="15" viewBox="0 0 24 24" fill="#fff"><path d="M6.6 10.8a15 15 0 0 0 6.6 6.6l2.2-2.2c.3-.3.7-.4 1-.2 1.1.4 2.3.6 3.6.6.6 0 1 .4 1 1V20c0 .6-.4 1-1 1A17 17 0 0 1 3 4c0-.6.4-1 1-1h3.5c.6 0 1 .4 1 1 0 1.3.2 2.5.6 3.6.1.3 0 .7-.2 1z"/></svg>
      </span>
    </div>
    <div class="contact contact-mail">
      <span class="contact-text">info@meridianfield.co</span>
      <span class="contact-icon">
        <svg width="17" height="13" viewBox="0 0 18 14" fill="none" stroke="#fff" stroke-width="1.6"><rect x="1" y="1" width="16" height="12"/><path d="M1 1l8 6 8-6"/></svg>
      </span>
    </div>
  </article>
</div>
</body>
</html>
```